8 1/2 x 8 1/2 Social Media Design Ad - Commercial Loan Originator

Wanted
Commercial Loan Originators

* No Licensing Required
* Lend Nationwide with few exceptions
* Competitive Compensation
* You find the Investors and we handle the rest!!!

PRODUCTS
* Debt Service Coverage Loans (DSCR)
* Fix & Flip Financing
* Ground Up Construction
* Bridge Loans
* Portfolio Loans
And many more.....

Call (800) 417-9265 x24 for more information

Brightmoor Lending Partners, Inc.
7200 Warbleton Avenue, Ellicott City, MD 21043
NMLS #318640

```html
<!DOCTYPE html>
<html lang="en">
<head>
<meta charset="utf-8">
<title>Now Hiring – Commercial Loan Originators</title>
<link href="https://fonts.googleapis.com/css2?family=Playfair+Display:wght@700&family=Montserrat:wght@400;500&display=swap" rel="stylesheet">
<style>
  :root {
    --page-bg: #c0d6e4;
    --navy-deep: #17233a;
    --navy-mid: #2c3d58;
    --sky: #6f8fb0;
    --house: #8d95a0;
    --gold-light: #f3e2a0;
    --gold: #d6b764;
    --gold-dark: #a9853a;
    --white: #ffffff;
    --text-soft: #eef1f6;
  }
  * { margin: 0; padding: 0; box-sizing: border-box; }
  html, body { width: 1200px; height: 800px; overflow: hidden; }
  body {
    background: var(--page-bg);
    font-family: "Montserrat", Arial, sans-serif;
    position: relative;
  }
  .ad {
    position: absolute;
    left: 240px; top: 40px;
    width: 720px; height: 720px;
    overflow: hidden;
    box-shadow: 8px 10px 18px rgba(0,0,0,0.25);
  }
  .ad-photo {
    position: absolute; inset: 0;
    background:
      linear-gradient(90deg, rgba(23,35,58,0.92) 0%, rgba(23,35,58,0.78) 42%, rgba(23,35,58,0.15) 70%, rgba(23,35,58,0) 100%),
      radial-gradient(ellipse 30% 45% at 72% 55%, #2e3b52 0%, rgba(46,59,82,0) 100%),
      linear-gradient(180deg, var(--sky) 0%, var(--house) 35%, var(--navy-mid) 70%, var(--navy-deep) 100%);
  }
  .brand {
    position: absolute; left: 0; width: 430px; top: 60px;
    text-align: center;
  }
  .brand-mark {
    width: 70px; height: 70px; border-radius: 50%;
    border: 3px solid var(--gold);
    margin: 0 auto 12px;
  }
  .brand-name {
    font-family: "Playfair Display", Georgia, serif;
    font-weight: 700; font-size: 22px;
    color: var(--gold);
    letter-spacing: 0.5px;
  }
  .brand-tagline {
    font-size: 8px; color: var(--gold-light);
    letter-spacing: 1px; margin-top: 4px; text-transform: uppercase;
  }
  .brand-est {
    font-size: 9px; color: var(--gold-light);
    letter-spacing: 2px; margin-top: 4px;
  }
  .hiring-band {
    position: absolute; left: 60px; top: 250px;
    width: 300px; height: 27px;
    background: linear-gradient(90deg, rgba(214,183,100,0) 0%, var(--gold-light) 20%, var(--gold) 80%, rgba(214,183,100,0) 100%);
    color: var(--navy-deep);
    font-size: 22px; font-weight: 500; letter-spacing: 1px;
    text-align: center; line-height: 27px;
  }
  .headline {
    position: absolute; left: 0; width: 430px; top: 305px;
    font-family: "Playfair Display", Georgia, serif;
    font-weight: 700; font-size: 44px; line-height: 51px;
    color: var(--white); text-align: center; letter-spacing: -1px;
  }
  .rule {
    position: absolute; left: 40px; width: 350px; height: 1px;
    background: linear-gradient(90deg, rgba(214,183,100,0), var(--gold), rgba(214,183,100,0));
  }
  .rule-top { top: 431px; }
  .rule-bottom { top: 475px; }
  .pitch {
    position: absolute; left: 0; width: 430px; top: 444px;
    text-align: center; font-size: 15px; letter-spacing: 1px;
    color: var(--text-soft);
  }
  .benefits {
    position: absolute; left: 68px; top: 500px;
    list-style: none;
  }
  .benefits li {
    display: flex; align-items: center; gap: 12px;
    font-size: 17px; letter-spacing: 1.5px; color: var(--text-soft);
    height: 34px;
  }
  .benefits svg { width: 17px; height: 17px; }
  .cta {
    position: absolute; left: 56px; top: 590px;
    width: 314px; height: 47px;
    background: linear-gradient(180deg, var(--gold-light) 0%, var(--gold) 55%, var(--gold-dark) 100%);
    border: 2px solid var(--gold-dark);
    border-radius: 3px;
    color: var(--navy-deep);
    font-size: 24px; font-weight: 500;
    display: flex; align-items: center; justify-content: center;
  }
  .cta small { font-size: 15px; margin-left: 6px; margin-top: 5px; }
</style>
</head>
<body>
  <section class="ad">
    <div class="ad-photo" role="img" aria-label="Smiling businessman in a grey suit with arms crossed, standing in front of a suburban house under a blue sky"></div>

    <header class="brand">
      <div class="brand-mark"></div>
      <div class="brand-name">Brightmoor Lending Partners</div>
      <div class="brand-tagline">Your trusted partner in commercial lending nationwide</div>
      <div class="brand-est">EST. 1992</div>
    </header>

    <div class="hiring-band">NOW HIRING</div>

    <h1 class="headline">Commercial Loan<br>Originators</h1>

    <div class="rule rule-top"></div>
    <p class="pitch">You find the investors. We handle the rest.</p>
    <div class="rule rule-bottom"></div>

    <ul class="benefits">
      <li>
        <svg viewBox="0 0 20 20" fill="none" stroke="#eef1f6" stroke-width="1.8"><circle cx="10" cy="10" r="8"/><path d="M6 10.5l3 3 7-8"/></svg>
        No Licensing Required
      </li>
      <li>
        <svg viewBox="0 0 20 20" fill="none" stroke="#eef1f6" stroke-width="1.8"><circle cx="10" cy="10" r="8"/><path d="M6 10.5l3 3 7-8"/></svg>
        Competitive Compensation
      </li>
    </ul>

    <div class="cta">Call (800) 417-9265 <small>x24</small></div>
  </section>
</body>
</html>
```